Logo and Business card design!

Welbrook Estates

We are a Property development and real estate company (needs a logo design).

Welbrook estates is based in Sydney Australia and will be dealing with high net worth individuals with a corporate background. The demographic of clients will be relatively youthful and savvy. We do development finance, property development and some portion of property sales

I'd like the 'Welbrook' part of the name to be strength of the title, with 'property' playing a very minor part, perhaps in tiny font somewhere off to the bottom or side or something

Thank you!

Target Market(s)

25-55 years old

Industry/Entity Type

Real Estate Development

Contact Information for Business Card

Please arrange this information as you see fit

Leon Brightwater
Managing Director
0417 582 273
leon@welbrookestates-example.com.au
www.welbrookestates-example.com.au

Logo Text

Welbrook estates

Font styles to use
Serif

Colors

Designer to choose colors to be used in the design.

Requirements
Must have
• PLEASE VIEW THE UPLOADED IMAGES AND EXAMPLES
• And please put 'property' in small letters at the bottom or to the side. I want it to play a minimalist role, with 'WELBROOK' being the feature
• Colours! Please make sure theyre mostly grey and white with possibly some other dark blue and maybe dark grey
Nice to have
• Please feel free to use whatever colors you like, the suggested colors are something I selected momentarily and dont necessarily reflect strict guidelines
Should not have
• NO pictures or shapes of houses. I dont want the logo design to be so literal in its imagery

```html
<!DOCTYPE html>
<html lang="en">
<head>
<meta charset="utf-8">
<title>Welbrook Estates – Logo and Business Card</title>
<link rel="stylesheet" href="https://fonts.googleapis.com/css2?family=Jost:wght@300&display=swap">
<style>
  :root {
    --paper: #ffffff;
    --ink: #111111;
    --stone: #a7a39e;
    --stone-soft: #9b9791;
    --frame: #dddddd;
  }
  * { margin: 0; padding: 0; box-sizing: border-box; }
  html, body {
    width: 804px; height: 1200px; overflow: hidden;
    background: var(--paper);
    font-family: "Jost", "Futura", sans-serif;
    font-weight: 300;
  }
  .sheet { position: relative; width: 804px; height: 1200px; }

  .card {
    position: absolute; left: 38px; width: 728px; height: 428px;
    border: 1px solid var(--frame); overflow: hidden; background: var(--paper);
  }
  .card--front { top: 105px; }
  .card--back { top: 717px; }

  /* Front */
  .front-band {
    position: absolute; left: 0; right: 0; top: 308px; height: 120px;
    background: var(--ink);
  }
  .front-band__stripe {
    position: absolute; left: 0; right: 0; top: 28px; height: 24px;
    background: var(--stone);
  }
  .wordmark { position: absolute; color: var(--ink); font-weight: 300; line-height: 1; }
  .wordmark__name { display: block; letter-spacing: 0.02em; }
  .wordmark__tag { display: block; letter-spacing: 0.04em; }
  .wordmark--front { left: 156px; top: 150px; }
  .wordmark--front .wordmark__name { font-size: 80px; }
  .wordmark--front .wordmark__tag { font-size: 26px; margin: 8px 0 0 66px; }

  /* Back */
  .back-edge { position: absolute; left: 0; top: 0; width: 17px; height: 100%; background: var(--ink); }
  .back-panel { position: absolute; left: 332px; top: 0; right: 0; height: 100%; background: var(--ink); }
  .notch { position: absolute; }
  .notch--out { left: 332px; top: 94px; }
  .notch--in { left: 297px; top: 342px; }

  .wordmark--back { left: 54px; top: 92px; }
  .wordmark--back .wordmark__name { font-size: 48px; }
  .wordmark--back .wordmark__tag { font-size: 16px; margin: 4px 0 0 40px; }

  .holder { position: absolute; right: 59px; top: 96px; text-align: right; }
  .holder__name { color: var(--paper); font-size: 29px; font-weight: 300; line-height: 1.1; }
  .holder__role { color: var(--stone-soft); font-size: 15px; margin-top: 8px; }

  .contacts { position: absolute; left: 374px; top: 282px; list-style: none; }
  .contacts__item { display: flex; align-items: center; height: 37px; color: var(--paper); font-size: 16px; }
  .contacts__icon { width: 26px; height: 26px; margin-right: 33px; flex: none; }
</style>
</head>
<body>
<main class="sheet">

  <section class="card card--front" aria-label="Front of business card">
    <div class="wordmark wordmark--front">
      <span class="wordmark__name">WELBROOK</span>
      <span class="wordmark__tag">ESTATES</span>
    </div>
    <div class="front-band"><div class="front-band__stripe"></div></div>
  </section>

  <section class="card card--back" aria-label="Back of business card">
    <div class="back-edge"></div>
    <div class="back-panel"></div>
    <svg class="notch notch--out" width="34" height="40" viewBox="0 0 34 40"><polygon points="0,0 34,20 0,40" fill="#ffffff"/></svg>
    <svg class="notch notch--in" width="36" height="38" viewBox="0 0 36 38"><polygon points="36,0 0,19 36,38" fill="#111111"/></svg>

    <div class="wordmark wordmark--back">
      <span class="wordmark__name">WELBROOK</span>
      <span class="wordmark__tag">ESTATES</span>
    </div>

    <div class="holder">
      <p class="holder__name">Leon Brightwater</p>
      <p class="holder__role">Managing Director</p>
    </div>

    <ul class="contacts">
      <li class="contacts__item">
        <svg class="contacts__icon" viewBox="0 0 26 26" aria-hidden="true">
          <circle cx="13" cy="13" r="13" fill="#a7a39e"/>
          <rect x="9" y="6" width="8" height="14" rx="1.5" fill="none" stroke="#111" stroke-width="1.6"/>
          <line x1="11.5" y1="17.5" x2="14.5" y2="17.5" stroke="#111" stroke-width="1.4"/>
        </svg>
        0417 582 273
      </li>
      <li class="contacts__item">
        <svg class="contacts__icon" viewBox="0 0 26 26" aria-hidden="true">
          <circle cx="13" cy="13" r="13" fill="#a7a39e"/>
          <g fill="none" stroke="#111" stroke-width="1.2">
            <circle cx="13" cy="13" r="6.5"/>
            <ellipse cx="13" cy="13" rx="3" ry="6.5"/>
            <line x1="6.5" y1="13" x2="19.5" y2="13"/>
            <line x1="7.5" y1="9.5" x2="18.5" y2="9.5"/>
            <line x1="7.5" y1="16.5" x2="18.5" y2="16.5"/>
          </g>
        </svg>
        www.welbrookestates-example.com.au
      </li>
      <li class="contacts__item">
        <svg class="contacts__icon" viewBox="0 0 26 26" aria-hidden="true">
          <circle cx="13" cy="13" r="13" fill="#a7a39e"/>
          <g fill="none" stroke="#111" stroke-width="1.5">
            <rect x="6.5" y="8.5" width="13" height="9"/>
            <polyline points="6.5,8.5 13,14 19.5,8.5"/>
          </g>
        </svg>
        leon@welbrookestates-example.com.au
      </li>
    </ul>
  </section>

</main>
</body>
</html>
```